Business Cards + Flyer + Letterhead for Care Recruitment Agency

We are a recruitment agency for the health & care sector. We need designs made for business cards, A5 double-sided flyer, and a letterhead template.

Our branding message is professionalism, care, compassion, expertise. We are experts in recruitment for the care & health industry.

Our logo source files and colours are here - https://www.fileporta.net/sh/qrvn82lopx4kdte/BBBgKy8LMQ27uTnPwZxHcVobsa?dl=0

For the business card, I have attached an example we like. We want a vertical business card design, something very similar to the example given. The design should match our logo in terms of brand colors. On one side should be our logo, our website (www.hollowmere.co.uk) and Care Recruitment Specialists written somewhere visible that fits, between our logo and the website at the bottom. On the other side should be our details.

Details on the front:

Logo with slogan
Care Recruitment Specialists
www.hollowmere.co.uk

Details on the back:

Tobias Orlund
Managing Director

Pellam House, 31-39 Larkfield St, Birmingham, B4 7QD
07612 495371
tobias@hollowmere.co.uk
www.hollowmere.co.uk

Marnie Holloway
Business Development Director

07831 204968
marnie@hollowmere.co.uk
www.hollowmere.co.uk

For the A5 flyer, I have attached some pictures we've used for the website, which could be used for the flyer as well. To get a better idea of our branding, please visit our website - https://hollowmere.co.uk/

The text for the flyer is also attached.

Finally, the letterhead template should be a docx template with our logo and our identifiable branding (the same shapes and matching colours you will come up with for the business cards and flyer).

```html
<!DOCTYPE html>
<html lang="en">
<head>
<meta charset="utf-8">
<title>Hollowmere – Business Card</title>
<link rel="stylesheet" href="https://fonts.googleapis.com/css2?family=Bebas+Neue&family=Montserrat:wght@700&family=Poppins:wght@400&display=swap">
<style>
  :root {
    --stage: #e6e7e9;
    --card-light: #f5f6f8;
    --navy: #0b2d6b;
    --cyan: #1cb4e8;
    --ink: #45474c;
    --icon: #16336e;
    --front-top: #1f4c86;
    --front-mid: #0a3584;
    --front-bottom: #0b2862;
    --white: #ffffff;
  }
  * { box-sizing: border-box; margin: 0; padding: 0; }
  html, body {
    width: 1200px; height: 1200px; overflow: hidden;
    background: var(--stage);
  }
  .canvas { position: relative; width: 1200px; height: 1200px; }

  .card {
    position: absolute; top: 226px;
    width: 391px; height: 686px;
    border-radius: 20px; overflow: hidden;
  }

  /* Details side */
  .card--details {
    left: 195px;
    background: var(--card-light);
    font-family: "Poppins", sans-serif;
  }
  .holder-name {
    position: absolute; left: 46px; top: 52px;
    font-family: "Bebas Neue", sans-serif;
    font-size: 44px; line-height: 1; color: var(--navy);
    letter-spacing: 0.2px;
  }
  .holder-role {
    position: absolute; left: 46px; top: 89px;
    font-size: 15.5px; color: var(--cyan); line-height: 1.2;
  }
  .address {
    position: absolute; left: 51px; top: 514px;
    font-size: 15.5px; line-height: 19.5px; color: var(--ink);
    font-style: normal;
  }
  .contact-list {
    position: absolute; left: 51px; top: 586px;
    list-style: none; font-size: 15.5px; color: var(--ink);
  }
  .contact-list li {
    display: flex; align-items: center; height: 20px; gap: 10px;
  }
  .contact-list svg { width: 14px; height: 14px; flex: none; fill: var(--icon); }

  /* Brand side */
  .card--brand {
    left: 660px;
    background:
      radial-gradient(ellipse 75% 40% at 50% 55%, rgba(20, 80, 190, 0.55), rgba(20, 80, 190, 0) 70%),
      linear-gradient(180deg, var(--front-top) 0%, var(--front-mid) 45%, var(--front-bottom) 100%);
    text-align: center;
  }
  .brand-name {
    position: absolute; left: 0; right: 0; top: 366px;
    font-family: "Montserrat", sans-serif; font-weight: 700;
    font-size: 31px; letter-spacing: 3.5px; color: var(--white);
    line-height: 1;
  }
  .brand-tagline {
    position: absolute; left: 0; right: 0; top: 405px;
    font-family: "Poppins", sans-serif; font-size: 16px;
    color: var(--cyan); line-height: 1.2;
  }
</style>
</head>
<body>
<main class="canvas">

  <section class="card card--details">
    <h1 class="holder-name">Marnie Holloway</h1>
    <p class="holder-role">Business Development Director</p>

    <address class="address">
      Pellam House, 31-39<br>
      Larkfield St,<br>
      Birmingham, B4 7QD
    </address>

    <ul class="contact-list">
      <li>
        <svg viewBox="0 0 24 24" aria-hidden="true"><path d="M6.6 10.8a15.1 15.1 0 0 0 6.6 6.6l2.2-2.2a1 1 0 0 1 1-.25 11.4 11.4 0 0 0 3.6.57 1 1 0 0 1 1 1V20a1 1 0 0 1-1 1A17 17 0 0 1 3 4a1 1 0 0 1 1-1h3.5a1 1 0 0 1 1 1c0 1.25.2 2.45.57 3.57a1 1 0 0 1-.25 1z"/></svg>
        <span>07831 204968</span>
      </li>
      <li>
        <svg viewBox="0 0 24 24" aria-hidden="true"><path d="M2 5h20v14H2z M3.5 6.5 12 12.5l8.5-6z" fill-rule="evenodd"/></svg>
        <span>marnie@hollowmere.co.uk</span>
      </li>
      <li>
        <svg viewBox="0 0 24 24" aria-hidden="true"><path d="M12 2a10 10 0 1 0 0 20 10 10 0 0 0 0-20zm-1 17.9A8 8 0 0 1 4.2 10.2L9 15v1a2 2 0 0 0 2 2zm6.9-2.5A2 2 0 0 0 16 16h-1v-3a1 1 0 0 0-1-1H8v-2h2a1 1 0 0 0 1-1V7h2a2 2 0 0 0 2-2v-.4a8 8 0 0 1 2.9 12.8z"/></svg>
        <span>www.hollowmere.co.uk</span>
      </li>
    </ul>
  </section>

  <section class="card card--brand">
    <h2 class="brand-name">HOLLOWMERE</h2>
    <p class="brand-tagline">Care Recruitment Specialists</p>
  </section>

</main>
</body>
</html>
```